Mortgage Company needs some fresh looking business cards to replace current outdated design

Looking for fresh ideas. The only requirement is that the card must show the following:Keystead Logo (uploaded)Keystead slogan "home loans made clear"Fair Dwelling Creditor logo (uploaded)Keystead NMLS #583017 (see current bus card, uploaded)Website as shown on sampleColor Codes as follows:Green = PMS 555 , #2b7051 , CMYK 83 33 77 21Rust = PMS 471 , #bc6225 , CMYK 21 70 100 8Would like two sided card. Front will have all of the above info, and back will have just the logo.

Target Market(s)

Consumers and Real Estate Agents

Industry/Entity Type

Mortgage Lender

Contact Information for Business Card

Color Codes as follows:
Green = PMS 555 , #2b7051 , CMYK 83 33 77 21
Rust = PMS 471 , #bc6225 , CMYK 21 70 100 8

Would like two sided card. Front will have all of the above info, and back will have just the logo.

Requirements
Must have
• Keystead Logo (uploaded)
• Keystead slogan "home loans made clear"
• Fair Dwelling Creditor logo (uploaded)
• Keystead NMLS #583017 (see current bus card, uploaded)
• Website as shown on sample

```html
<!DOCTYPE html>
<html lang="en">
<head>
<meta charset="utf-8">
<title>Keystead Mortgage – Business Card</title>
<link href="https://fonts.googleapis.com/css2?family=Roboto:wght@400;500&display=swap" rel="stylesheet">
<style>
  :root {
    --green: #00684f;
    --green-soft: #dce8e3;
    --rust: #c8651b;
    --ink: #1b1b1b;
    --paper: #ffffff;
    --bg-light: #8c969b;
    --bg-dark: #4f585c;
  }
  * { box-sizing: border-box; margin: 0; padding: 0; }
  html, body { width: 1200px; height: 900px; overflow: hidden; }
  body {
    background: radial-gradient(ellipse at 50% 45%, var(--bg-light), var(--bg-dark));
    font-family: "Roboto", Arial, sans-serif;
    position: relative;
  }
  .card {
    position: absolute;
    width: 560px;
    height: 320px;
    border-radius: 22px;
    box-shadow: 0 10px 24px rgba(0,0,0,.35);
    overflow: hidden;
  }
  .card--back { left: 80px; top: 90px; background: var(--green); }
  .card--front { left: 560px; top: 480px; background: var(--paper); }

  .brand { position: absolute; line-height: 1; }
  .brand__slogan { display: block; font-weight: 400; letter-spacing: .5px; }
  .brand__name { display: block; font-weight: 500; }
  .brand__mark { display: inline-block; flex: none; border-radius: 50%; }
  .brand__row { display: flex; align-items: center; }

  .card--back .brand { left: 110px; top: 110px; color: var(--paper); }
  .card--back .brand__slogan { font-size: 18px; margin: 0 0 10px 70px; }
  .card--back .brand__row { gap: 16px; }
  .card--back .brand__mark { width: 54px; height: 54px; background: var(--paper); }
  .card--back .brand__name { font-size: 36px; color: var(--paper); }

  .card--front .brand { left: 34px; top: 30px; }
  .card--front .brand__slogan { font-size: 10px; color: var(--rust); margin: 0 0 5px 37px; }
  .card--front .brand__row { gap: 9px; }
  .card--front .brand__mark { width: 28px; height: 28px; background: var(--green); }
  .card--front .brand__name { font-size: 18px; color: var(--green); }

  .decor-circle {
    position: absolute; right: 90px; top: 18px;
    width: 100px; height: 100px; border-radius: 50%;
    background: var(--green-soft);
  }
  .nmls {
    position: absolute; right: 34px; top: 132px;
    font-size: 12px; line-height: 14px; color: var(--green); letter-spacing: .4px;
  }
  .divider {
    position: absolute; left: 34px; right: 30px; top: 152px;
    height: 2px; background: var(--rust);
  }
  .person { position: absolute; left: 34px; top: 108px; line-height: 1.1; }
  .person__name { font-size: 20px; color: var(--rust); font-weight: 500; letter-spacing: .3px; }
  .person__role { font-size: 11px; color: var(--ink); margin-top: 3px; }
  .address {
    position: absolute; right: 34px; top: 166px;
    font-size: 12px; color: var(--ink); text-align: right; line-height: 1.4;
  }
  .contact-list { position: absolute; left: 40px; top: 180px; list-style: none; }
  .contact-list li { display: flex; align-items: center; gap: 12px; font-size: 14px; color: var(--ink); height: 27px; }
  .contact-list svg { width: 21px; height: 21px; flex: none; }
</style>
</head>
<body>

<section class="card card--back" aria-label="Card back">
  <div class="brand">
    <span class="brand__slogan">home loans made clear</span>
    <div class="brand__row">
      <span class="brand__mark"></span>
      <span class="brand__name">Keystead Mortgage</span>
    </div>
  </div>
</section>

<section class="card card--front" aria-label="Card front">
  <div class="decor-circle" role="img" aria-label="Faint brand emblem decoration"></div>

  <div class="brand">
    <span class="brand__slogan">home loans made clear</span>
    <div class="brand__row">
      <span class="brand__mark"></span>
      <span class="brand__name">Keystead Mortgage</span>
    </div>
  </div>

  <p class="nmls">NMLS #583017</p>

  <div class="person">
    <p class="person__name">DANIEL MERCER</p>
    <p class="person__role">OWNER</p>
  </div>

  <div class="divider"></div>

  <p class="address">4820 Alder Crest Way<br>Brookvale, GA 30990</p>

  <ul class="contact-list">
    <li>
      <svg viewBox="0 0 20 20" aria-hidden="true"><rect width="20" height="20" fill="var(--green)"/><path d="M6 4l2.5 0 1 3-1.5 1c.8 1.7 2 2.9 3.7 3.7l1-1.5 3 1V14c0 1-1 2-2 2C8.5 16 4 11.5 4 6c0-1 1-2 2-2z" fill="#fff"/></svg>
      555-014-2278
    </li>
    <li>
      <svg viewBox="0 0 20 20" aria-hidden="true"><rect width="20" height="20" fill="var(--green)"/><rect x="5" y="9" width="10" height="6" rx="1" fill="#fff"/><path d="M4 8c0-3 12-3 12 0v1h-3V7.5c-2-.7-4-.7-6 0V9H4z" fill="#fff"/></svg>
      555-019-6630
    </li>
    <li>
      <svg viewBox="0 0 20 20" aria-hidden="true"><rect width="20" height="20" fill="var(--green)"/><rect x="4" y="6" width="12" height="8" fill="#fff"/><path d="M4 6l6 5 6-5" fill="none" stroke="var(--green)" stroke-width="1.2"/></svg>
      dmercer@keysteadmail.com
    </li>
    <li>
      <svg viewBox="0 0 20 20" aria-hidden="true"><rect width="20" height="20" fill="var(--green)"/><circle cx="10" cy="10" r="5.5" fill="none" stroke="#fff" stroke-width="1.3"/><path d="M4.5 10h11M10 4.5c-2.5 3-2.5 8 0 11M10 4.5c2.5 3 2.5 8 0 11" fill="none" stroke="#fff" stroke-width="1"/></svg>
      www.keysteadlending.com
    </li>
  </ul>
</section>

</body>
</html>
```